Company Real Estate Site Needs A Face Lift

I need a new website for the recent company I formed: Voska Real Estate.
You can use my agent website WWW.PALMIROQ.COM to see the style/brand I already have. I will have areas for Searching for homes on IDX, etc.
I really like this site:
http://www.cranfeltmanorhomes.com/
I have attached my logo as well

Industry/Entity Type

Real Estate

Colors
0255a3
ffffff
cee9f5

```html
<!DOCTYPE html>
<html lang="en">
<head>
<meta charset="utf-8">
<title>Voska Real Estate</title>
<link href="https://fonts.googleapis.com/css2?family=Lato:wght@300;400;700&display=swap" rel="stylesheet">
<style>
:root{
  --brand:#0255a3;
  --brand-bright:#1a8ee0;
  --sky:#cee9f5;
  --teal:#2fc6d6;
  --ink:#2b2b2b;
  --muted:#555;
  --dark:#1d1d1d;
  --darker:#141414;
  --white:#ffffff;
  --page:#f5f6f7;
  --line:#d9dde1;
}
*{box-sizing:border-box;margin:0;padding:0}
html,body{width:941px;height:1200px;overflow:hidden;background:var(--white)}
body{font-family:'Lato',sans-serif;color:var(--ink)}
.site{position:relative;width:941px;height:1200px;overflow:hidden;background:var(--page)}

/* header */
.header{position:absolute;left:0;top:0;width:941px;height:125px;background:linear-gradient(180deg,#050505 0%,#151515 70%,#2a2a2a 100%)}
.header-sheen{position:absolute;left:0;top:0}
.brand{position:absolute;left:108px;top:40px;display:flex;align-items:center;gap:10px;color:var(--white);font-weight:700;font-size:26px;letter-spacing:.5px}
.brand-dot{width:22px;height:22px;border-radius:50%;background:var(--teal)}
.contact-top{position:absolute;left:708px;top:22px;color:var(--white);font-size:12px;line-height:16px}
.follow{position:absolute;left:661px;top:96px;display:flex;align-items:center;gap:6px;color:var(--white);font-size:15px}
.follow span{margin-right:5px}
.social-dot{width:20px;height:20px;border-radius:50%;background:var(--white)}

/* navigation */
.nav{position:absolute;left:0;top:125px;width:941px;height:37px;background:linear-gradient(180deg,#1f8fe0 0%,#0a62b8 100%);display:flex;padding-left:103px}
.nav a{display:flex;align-items:center;justify-content:center;color:var(--white);font-size:11.5px;font-weight:700;text-decoration:none;border-right:1px solid rgba(0,0,0,.18)}
.nav a.active{background:linear-gradient(180deg,#e9f5fc 0%,var(--sky) 100%);color:var(--brand)}

/* hero */
.hero{position:absolute;left:0;top:162px;width:941px;height:368px;background:linear-gradient(180deg,#bcd3e4 0%,#9eb3bf 35%,#6c7a6a 65%,#4f7a3a 82%,#6f8f83 100%)}
.hero-arrow{position:absolute;left:82px;top:167px}
.caption{position:absolute;left:103px;top:191px;width:320px;height:132px;background:rgba(20,20,20,.82);border-radius:0 0 12px 0;padding:12px 16px}
.caption h1{font-weight:300;font-size:31px;color:var(--white);line-height:38px}
.caption p{font-size:11.5px;color:var(--white);line-height:16px;margin-top:6px}
.btn-estimate{position:absolute;left:17px;top:93px;width:124px;height:22px;background:var(--brand-bright);color:var(--white);font-size:10.5px;font-weight:700;display:flex;align-items:center;justify-content:center}
.dots{position:absolute;left:249px;top:100px;display:flex;gap:6px}
.dots i{width:11px;height:11px;border-radius:50%;background:#bfbfbf}
.dots i.on{background:var(--brand-bright);box-shadow:0 0 0 2px var(--white)}

.search{position:absolute;left:635px;top:67px;width:201px;height:253px;background:var(--white);border:2px solid var(--teal);box-shadow:0 0 8px rgba(47,198,214,.5)}
.search-head{height:38px;background:linear-gradient(180deg,#1f8fe0,#0a62b8);display:flex;align-items:center;padding-left:16px;gap:10px;color:var(--white);font-size:15px}
.search-body{position:relative;padding:0 16px;font-size:10px;color:var(--ink)}
.lbl{position:absolute}
.field{position:absolute;height:16px;border:1px solid #bdbdbd;background:var(--white)}
.field.sel::after{content:"";position:absolute;right:0;top:0;width:14px;height:14px;background:linear-gradient(#ececec,#c9c9c9)}
.field.sel::before{content:"";position:absolute;right:4px;top:5px;border:3px solid transparent;border-top:4px solid #666;z-index:1}
.btn-search{position:absolute;left:15px;top:213px;width:59px;height:21px;background:var(--brand);color:var(--white);font-size:10px;font-weight:700;display:flex;align-items:center;justify-content:center}
.adv{position:absolute;left:85px;top:218px;color:var(--brand);font-size:8.5px;text-decoration:underline}

/* services */
.services{position:absolute;left:103px;top:557px;width:734px;display:flex;justify-content:space-between}
.service{width:176px;text-align:center}
.service-icon{width:68px;height:68px;margin:0 auto;border-radius:50%;background:var(--white);border:1px solid #dcdcdc;box-shadow:0 1px 3px rgba(0,0,0,.12);display:flex;align-items:center;justify-content:center}
.service h2{font-size:15px;font-weight:400;margin-top:6px;color:var(--ink)}
.service h2 b{font-weight:400;color:var(--brand)}
.service p{font-size:10px;line-height:15.5px;color:var(--muted);margin-top:4px}
.more{display:inline-block;font-size:10px;color:var(--brand);margin-top:4px}
.divider{position:absolute;left:125px;top:745px;width:690px;height:1px;background:linear-gradient(90deg,transparent,#b9cfe0,transparent)}

/* listings */
.featured-title{position:absolute;left:0;top:763px;width:941px;text-align:center;font-size:28px;font-weight:300;color:var(--brand)}
.listings{position:absolute;left:103px;top:818px;width:734px;display:flex;justify-content:space-between}
.listing{width:171px;font-size:10px}
.listing-photo{height:97px;border:1px solid #dcdcdc;background:var(--white);padding:3px}
.listing-photo div{width:100%;height:100%;background:linear-gradient(180deg,#9ec4e4 0%,#bcd4e6 30%,#8b6e5e 55%,#6d8a4a 85%,#4f7336 100%)}
.cost{margin-top:9px;font-size:10px}
.row{display:flex;justify-content:space-between;border-bottom:1px solid var(--line);padding:5px 0 3px;color:var(--ink)}
.row span:last-child{color:var(--muted)}

/* footer */
.footer{position:absolute;left:0;top:1007px;width:941px;height:155px;background:var(--dark)}
.about{position:absolute;left:104px;top:32px;width:340px}
.foot-title{display:flex;align-items:center;gap:8px;color:var(--white);font-size:14px}
.foot-title i{width:20px;height:20px;border-radius:50%;border:2px solid var(--brand-bright)}
.about p{font-size:10px;color:#7a7a7a;line-height:15.5px;margin-top:6px}
.contact-detail{position:absolute;left:500px;top:35px;width:170px;font-size:10px;color:#7a7a7a;line-height:15.5px}
.contact-detail h3{font-size:14px;font-weight:400;color:var(--white);margin-bottom:6px}
.contact-detail .co{color:var(--brand-bright);letter-spacing:.5px}
.cline{display:flex;align-items:center;gap:9px;margin-top:3px}
.foot-brand{position:absolute;left:697px;top:63px;display:flex;align-items:center;gap:8px;color:var(--white);font-weight:700;font-size:17px}
.foot-brand i{width:16px;height:16px;border-radius:50%;background:var(--teal)}
.copy{position:absolute;left:697px;top:128px;font-size:8.5px;color:#777}
.bottom{position:absolute;left:0;top:1162px;width:941px;height:38px;background:var(--darker);display:flex;align-items:center;padding-left:104px}
.bottom a{color:#cfcfcf;font-size:9px;text-decoration:none;padding:0 8px;border-left:1px solid #444}
.bottom a:first-child{padding-left:0;border-left:none}
.bottom .socials{position:absolute;left:716px;top:9px;display:flex;gap:7px}
</style>
</head>
<body>
<div class="site">

  <header class="header">
    <svg class="header-sheen" width="941" height="125" viewBox="0 0 941 125" aria-hidden="true">
      <path d="M58 0 L100 110 L941 78 L941 125 L0 125 L0 0 Z" fill="#2c2c2c"/>
      <path d="M58 0 L66 0 L104 106 L100 110 Z" fill="#6a6a6a"/>
    </svg>
    <div class="brand"><span class="brand-dot"></span>Voska Real Estate</div>
    <div class="contact-top">1-200-555-01928<br>info@voskarealestate.com</div>
    <div class="follow"><span>Follow Us</span><i class="social-dot"></i><i class="social-dot"></i><i class="social-dot"></i><i class="social-dot"></i></div>
  </header>

  <nav class="nav">
    <a class="active" style="width:81px">HOME</a>
    <a style="width:101px">COMPANY</a>
    <a style="width:65px">BUY</a>
    <a style="width:75px">SELL</a>
    <a style="width:125px">TESTIMONIALS</a>
    <a style="width:76px">BLOG</a>
    <a style="width:109px">RESOURCES</a>
    <a style="width:102px;border-right:none">CONTACT</a>
  </nav>

  <section class="hero" role="img" aria-label="Large white two-storey house with grey roof beside a lawn and pond">
    <svg class="hero-arrow" width="20" height="40" viewBox="0 0 20 40" aria-hidden="true"><path d="M18 2 L2 20 L18 38" fill="none" stroke="#fff" stroke-width="1.5"/></svg>
    <div class="caption">
      <h1>VOSKA Real Estate</h1>
      <p>Lorem ipsum dolor sit amet, consectetuer dopli adipisc cing elit, sed diam nonummy nibh.</p>
      <div class="btn-estimate">FREE ESTIMATE NOW</div>
      <div class="dots"><i class="on"></i><i></i><i></i><i></i></div>
    </div>

    <form class="search">
      <div class="search-head">
        <svg width="28" height="24" viewBox="0 0 28 24" aria-hidden="true"><path d="M14 1 L27 12 L23 12 L23 23 L5 23 L5 12 L1 12 Z" fill="#fff"/><rect x="12" y="14" width="5" height="9" fill="#0a62b8"/></svg>
        Find Your Property
      </div>
      <div class="search-body">
        <span class="lbl" style="left:15px;top:17px">Price per month</span>
        <span class="field" style="left:15px;top:33px;width:74px"></span>
        <span class="lbl" style="left:96px;top:35px">to</span>
        <span class="field" style="left:110px;top:33px;width:74px"></span>
        <span class="lbl" style="left:15px;top:54px">Location</span>
        <span class="field sel" style="left:15px;top:70px;width:169px"></span>
        <span class="lbl" style="left:15px;top:91px">Location</span>
        <span class="field sel" style="left:15px;top:107px;width:74px"></span>
        <span class="lbl" style="left:110px;top:91px">Location</span>
        <span class="field sel" style="left:110px;top:107px;width:74px"></span>
        <span class="lbl" style="left:15px;top:128px">Availability</span>
        <span class="field sel" style="left:15px;top:144px;width:74px"></span>
        <span class="lbl" style="left:110px;top:128px">Furnidhed</span>
        <span class="field sel" style="left:110px;top:144px;width:74px"></span>
      </div>
      <div class="btn-search">SEARCH</div>
      <span class="adv">Advanced Search</span>
    </form>
  </section>

  <section class="services">
    <article class="service">
      <div class="service-icon"><svg width="34" height="34" viewBox="0 0 34 34" aria-hidden="true"><path d="M4 16 L17 4 L30 16 M8 13 V30 H26 V13" fill="none" stroke="#333" stroke-width="2.5"/><path d="M11 19 L16 24 L26 12" fill="none" stroke="#333" stroke-width="3"/></svg></div>
      <h2><b>Property</b> Management</h2>
      <p>Lorem ipsum dolor sit amet, consectetuer adipiscing elit, sed diam nonummy nibh euismod volutpat.</p>
      <span class="more">Read More ▸</span>
    </article>
    <article class="service">
      <div class="service-icon"><svg width="34" height="34" viewBox="0 0 34 34" aria-hidden="true"><path d="M6 15 L17 5 L28 15 M10 12 V26 H24 V12" fill="none" stroke="#333" stroke-width="2.2"/><rect x="14" y="14" width="6" height="6" fill="#333"/><path d="M4 30 H30" stroke="#333" stroke-width="2"/></svg></div>
      <h2><b>Real Estate</b> Services</h2>
      <p>Lorem ipsum dolor sit amet, consectetuer adipiscing elit, sed diam nonummy nibh euismod volutpat.</p>
      <span class="more">Read More ▸</span>
    </article>
    <article class="service">
      <div class="service-icon"><svg width="34" height="34" viewBox="0 0 34 34" aria-hidden="true"><circle cx="19" cy="14" r="11" fill="#333"/><text x="19" y="19" font-family="Lato,sans-serif" font-size="14" font-weight="700" fill="#fff" text-anchor="middle">$</text><path d="M3 26 Q12 22 18 27 H30 Q26 32 18 31 H3 Z" fill="#333"/></svg></div>
      <h2><b>Renting</b> Collection</h2>
      <p>Lorem ipsum dolor sit amet, consectetuer adipiscing elit, sed diam nonummy nibh euismod volutpat.</p>
      <span class="more">Read More ▸</span>
    </article>
    <article class="service">
      <div class="service-icon"><svg width="30" height="36" viewBox="0 0 30 36" aria-hidden="true"><rect x="2" y="1" width="26" height="34" rx="3" fill="#333"/><rect x="6" y="5" width="18" height="7" fill="#fff"/><g fill="#fff"><rect x="6" y="15" width="4" height="4"/><rect x="13" y="15" width="4" height="4"/><rect x="20" y="15" width="4" height="4"/><rect x="6" y="22" width="4" height="4"/><rect x="13" y="22" width="4" height="4"/><rect x="20" y="22" width="4" height="4"/><rect x="6" y="29" width="4" height="3"/><rect x="13" y="29" width="4" height="3"/><rect x="20" y="29" width="4" height="3"/></g></svg></div>
      <h2><b>Loan</b> Calculator</h2>
      <p>Lorem ipsum dolor sit amet, consectetuer adipiscing elit, sed diam nonummy nibh euismod volutpat.</p>
      <span class="more">Read More ▸</span>
    </article>
  </section>

  <div class="divider"></div>
  <h2 class="featured-title">Featured Listings</h2>

  <section class="listings">
    <article class="listing">
      <div class="listing-photo"><div role="img" aria-label="Grey stone house with gabled roof"></div></div>
      <p class="cost">Cost : $310 000</p>
      <div class="row"><span>House Size:</span><span>2, 800 Sq Ft</span></div>
      <div class="row"><span>Lot size</span><span>0.20 Acres</span></div>
    </article>
    <article class="listing">
      <div class="listing-photo"><div role="img" aria-label="Red brick family house with garden"></div></div>
      <p class="cost">Cost : $310 000</p>
      <div class="row"><span>House Size:</span><span>2, 800 Sq Ft</span></div>
      <div class="row"><span>Lot size</span><span>0.20 Acres</span></div>
    </article>
    <article class="listing">
      <div class="listing-photo"><div role="img" aria-label="Beige two-storey house with driveway"></div></div>
      <p class="cost">Cost : $310 000</p>
      <div class="row"><span>House Size:</span><span>2, 800 Sq Ft</span></div>
      <div class="row"><span>Lot size</span><span>0.20 Acres</span></div>
    </article>
    <article class="listing">
      <div class="listing-photo"><div role="img" aria-label="Dark red brick house with white windows"></div></div>
      <p class="cost">Cost : $310 000</p>
      <div class="row"><span>House Size:</span><span>2, 800 Sq Ft</span></div>
      <div class="row"><span>Lot size</span><span>0.20 Acres</span></div>
    </article>
  </section>

  <footer class="footer">
    <div class="about">
      <div class="foot-title"><i></i>Shortly About Us</div>
      <p>Duis autem vel eum iriure dolor in hendrerit in vulputate velitasol esse molestie consequat, vel illum dolore eu feugiat nulla facilisisl at vero eros et accumsan et iusto odio dignissim qui blandit dollar praesent luptatum zzril delenit augue duis dolore te feugait dignissim qui blandit dollar praesent luptatum zzril delenit augue duis dolore te feugait nullar facilisi.</p>
    </div>
    <div class="contact-detail">
      <h3>Contact Detail</h3>
      <div class="co">VOSKA REAL ESTATE</div>
      <div>Duis autem vel eum iriure<br>dolor in hendrer</div>
      <div class="cline"><svg width="10" height="10" viewBox="0 0 10 10" aria-hidden="true"><path d="M2 1 L4 1 L5 3 L4 4 Q5 6 6 6 L7 5 L9 6 L9 8 Q8 9 6 9 Q1 7 1 2 Z" fill="#888"/></svg>1-200-555-01928</div>
      <div class="cline"><svg width="11" height="8" viewBox="0 0 11 8" aria-hidden="true"><rect width="11" height="8" fill="#888"/><path d="M0 0 L5.5 4.5 L11 0" fill="none" stroke="#1d1d1d"/></svg>info@voskarealestate.com</div>
    </div>
    <div class="foot-brand"><i></i>Voska Real Estate</div>
    <div class="copy">Copyright © 2014 Voska Real Estate.</div>
  </footer>

  <div class="bottom">
    <a>HOME</a><a>COMPANY</a><a>BUY</a><a>SELL</a><a>TESTIMONIALS</a><a>BLOG</a><a>RESOURCES</a><a>CONTACT</a>
    <div class="socials"><i class="social-dot"></i><i class="social-dot"></i><i class="social-dot"></i><i class="social-dot"></i></div>
  </div>

</div>
</body>
</html>
```